Design Our Holiday Magic Coupon

Purpose - The purpose of this project is to create a festive, uplifting, and visually engaging physical coupon that will be mailed to our existing community and warm leads.
The intent is twofold: first, to spark delight and connection by offering a tangible, personal touch during the holiday season; and second, to encourage customers to explore and purchase our programs as they prepare for a strong start to 2026. This mailer is designed to re-engage past buyers, inspire current participants, and gently invite new momentum into their practice through a simple, friendly offer.

Project Description + Scope

This project includes the design and production of a printed coupon ( card format) featuring a 20% discount on purchases of $79 or more. The copy should feel warm, clear, and celebratory without urgency or pressure.

The front of the card will include the headline (“Live Your Best 2026”), bold discount information, and the coupon code JOLLYDAY20. The back will include a short message reinforcing the tone of possibility and ease, plus simple redemption instructions and the expiry date: December 31, 2025. Deliverables include print-ready artwork, color selection aligned with KH brand style.

one side
LIVE YOUR BEST 2026
Enjoy 20% OFF when you buy $79 or more.
Use code: JOLLYDAY20
Redeem until end of day December 31, 2025.

Back side - Move with clarity.
Heal with intelligence.
Lead with ease.
Thank you for being part of Kinetic Harmony.
Lots of love, Marla and the whole of Team Marla

Target Market(s)

yoga teachers, yoga lovers, mostly over 50 years, women

Font styles to use
Other font styles liked:
• see attached for feel

Colors
0054AA
0677BA
7BADD7
CADEEF
E8F1F8
0094D4
00A9DD
6FCCEA
C7EBF8
E9F6FB
00AB8E
00BBA5
67D7C9
C6EFE9
E9F9F6
EB3D1F
EC4F4E
F09395
F8D3D4
FCEDEE

Requirements
Nice to have
• see attached

```html
<!DOCTYPE html>
<html lang="en">
<head>
<meta charset="utf-8">
<title>Kinetic Harmony Holiday Coupon</title>
<link rel="stylesheet" href="https://fonts.googleapis.com/css2?family=Playfair+Display:wght@700;800&family=Poppins:wght@300;400;500;600;700&family=Great+Vibes&display=swap">
<style>
  :root {
    --backdrop: #dddce1;
    --card-top: #0f8ca0;
    --card-mid: #25639a;
    --card-bottom: #3d3a85;
    --ink-white: #ffffff;
    --band-indigo: #2a2686;
    --accent-cyan: #1ccaec;
    --rule: rgba(255,255,255,0.45);
  }
  * { box-sizing: border-box; margin: 0; padding: 0; }
  html, body {
    width: 676px; height: 1200px; overflow: hidden;
    background: var(--backdrop);
  }
  .sheet { position: relative; width: 676px; height: 1200px; }
  .card {
    position: absolute; left: 112px; width: 453px; height: 453px;
    background: linear-gradient(180deg, var(--card-top) 0%, var(--card-mid) 45%, var(--card-bottom) 90%);
    box-shadow: 0 6px 12px rgba(0,0,0,0.28);
    color: var(--ink-white);
    overflow: hidden;
  }
  .card--front { top: 105px; }
  .card--back { top: 642px; }

  .headline {
    position: absolute; font-family: "Playfair Display", Georgia, serif;
    font-weight: 800; line-height: 1; white-space: nowrap;
  }
  .headline--line1 { left: 48px; top: 44px; font-size: 63px; letter-spacing: -0.5px; }
  .headline--line2 { left: 49px; top: 97px; font-size: 67px; letter-spacing: -1px; }
  .year-band {
    position: absolute; left: 201px; top: 102px; width: 204px; height: 50px;
    background: var(--band-indigo); border-radius: 3px;
    font-family: "Playfair Display", Georgia, serif; font-weight: 700;
    font-size: 46px; line-height: 50px; text-align: center; letter-spacing: 12px;
    padding-left: 10px;
  }

  .offer { position: absolute; font-family: "Poppins", Arial, sans-serif; white-space: nowrap; line-height: 1; }
  .offer--enjoy { left: 129px; top: 180px; font-size: 32px; font-weight: 300; }
  .offer--percent { left: 128px; top: 210px; font-size: 48px; font-weight: 700; letter-spacing: -0.5px; }
  .offer--band {
    left: 120px; top: 249px; width: 217px; height: 29px;
    background: var(--band-indigo); border-radius: 2px;
    font-size: 24px; font-weight: 700; line-height: 30px; text-align: center;
  }
  .offer--threshold { left: 115px; top: 282px; font-size: 38px; font-weight: 500; }
  .threshold-amount { color: var(--accent-cyan); font-weight: 700; letter-spacing: -1px; }
  .threshold-currency { font-size: 18px; vertical-align: 16px; }

  .code-band {
    position: absolute; left: 121px; top: 343px; width: 211px; height: 30px;
    background: var(--band-indigo); border-radius: 3px;
    font-family: "Poppins", Arial, sans-serif; font-size: 15.5px; line-height: 31px;
    text-align: center; white-space: nowrap;
  }
  .code-band strong { font-weight: 700; margin-left: 3px; }
  .expiry {
    position: absolute; left: 0; width: 100%; top: 402px; text-align: center;
    font-family: "Poppins", Arial, sans-serif; font-size: 12.8px; font-weight: 500;
  }

  .mantra {
    position: absolute; left: 0; width: 100%; top: 60px; text-align: center;
    font-family: "Playfair Display", Georgia, serif; font-weight: 700;
    font-size: 37px; line-height: 40px;
  }
  .thanks {
    position: absolute; left: 0; width: 100%; top: 212px; text-align: center;
    font-family: "Great Vibes", cursive; font-size: 64px; line-height: 1;
    color: var(--accent-cyan);
  }
  .thanks-note {
    position: absolute; left: 0; width: 100%; top: 284px; text-align: center;
    font-family: "Poppins", Arial, sans-serif; font-size: 16px; font-weight: 500;
  }
  .signoff {
    position: absolute; left: 0; width: 100%; top: 352px; text-align: center;
    font-family: "Poppins", Arial, sans-serif;
  }
  .signoff-title {
    display: flex; align-items: center; justify-content: center; gap: 7px;
    font-size: 17px; font-weight: 600; line-height: 22px;
  }
  .signoff-title::before, .signoff-title::after {
    content: ""; width: 82px; height: 1px; background: var(--rule);
  }
  .signoff-names { font-size: 17px; font-weight: 400; line-height: 22px; }
</style>
</head>
<body>
<main class="sheet">
  <section class="card card--front" aria-label="Coupon front">
    <h1>
      <span class="headline headline--line1">LIVE YOUR</span>
      <span class="headline headline--line2">BEST</span>
      <span class="year-band">2026</span>
    </h1>
    <p class="offer offer--enjoy">ENJOY</p>
    <p class="offer offer--percent">20% OFF</p>
    <p class="offer offer--band">WHEN YOU BUY</p>
    <p class="offer offer--threshold"><span class="threshold-amount"><span class="threshold-currency">$</span>79</span> OR MORE</p>
    <p class="code-band">Use code: <strong>JOLLYDAY20</strong></p>
    <p class="expiry">Redeem until end of day December 31, 2025</p>
  </section>

  <section class="card card--back" aria-label="Coupon back">
    <p class="mantra">Move with clarity.<br>Heal with intelligence.<br>Lead with ease.</p>
    <p class="thanks">Thank you</p>
    <p class="thanks-note">for being part of Kinetic Harmony.</p>
    <div class="signoff">
      <p class="signoff-title">Lots of love</p>
      <p class="signoff-names">Marla and the whole of Team Marla</p>
    </div>
  </section>
</main>
</body>
</html>
```